Ever Ready Path

Have clients check their mortgage qualifications before they go looking for a mortgage lender. This program gains access to your lenders credit report / 3 scores without impacting your credit scores.

```html
<!DOCTYPE html>
<html lang="en">
<head>
<meta charset="utf-8">
<title>Ever Ready Path – Business Card</title>
<link rel="stylesheet" href="https://fonts.googleapis.com/css2?family=Poppins:wght@400;500;700&display=swap">
<style>
  :root {
    --brand-blue: #0a47c7;
    --brand-green: #06c26f;
    --leaf-green: #8fe47e;
    --paper: #ffffff;
    --backdrop: #c9c9c9;
    --shadow: rgba(0, 0, 0, 0.22);
  }
  * { box-sizing: border-box; margin: 0; padding: 0; }
  html, body { width: 1200px; height: 800px; overflow: hidden; }
  body {
    background: var(--backdrop);
    font-family: "Poppins", sans-serif;
    display: flex;
    align-items: center;
    justify-content: center;
    gap: 60px;
  }
  .card {
    width: 520px;
    height: 300px;
    border-radius: 22px;
    position: relative;
    overflow: hidden;
    box-shadow: 0 14px 30px var(--shadow);
  }

  /* Front */
  .card-front { background: var(--brand-blue); color: var(--paper); }
  .front-feature {
    position: absolute;
    left: 24px;
    bottom: -24px;
    width: 250px;
    height: 220px;
    border-radius: 28px;
    background: var(--paper);
  }
  .front-details {
    position: absolute;
    right: 30px;
    top: 28px;
    text-align: right;
  }
  .brand-name {
    font-weight: 500;
    font-size: 30px;
    letter-spacing: 0.5px;
    line-height: 1;
    color: var(--paper);
  }
  .person-name {
    margin-top: 14px;
    font-weight: 700;
    font-size: 19px;
    line-height: 1.1;
  }
  .person-title {
    font-size: 12px;
    color: var(--brand-green);
    font-weight: 500;
  }
  .address {
    margin-top: 12px;
    font-size: 11px;
    line-height: 1.35;
  }
  .contact-list {
    list-style: none;
    margin-top: 10px;
    font-size: 11px;
    line-height: 1.5;
  }
  .contact-list li {
    display: flex;
    align-items: center;
    justify-content: flex-end;
    gap: 7px;
  }
  .contact-icon { width: 11px; height: 11px; flex: none; }

  /* Back */
  .card-back {
    background: var(--paper);
    display: flex;
    align-items: center;
    justify-content: center;
  }
  .back-brand {
    font-weight: 500;
    font-size: 40px;
    color: var(--brand-blue);
    letter-spacing: 0.5px;
  }
</style>
</head>
<body>

  <section class="card card-front" aria-label="Business card front">
    <div class="front-feature"></div>
    <div class="front-details">
      <p class="brand-name">Ever Ready Path</p>
      <p class="person-name">Dana Whitlock</p>
      <p class="person-title">President</p>
      <p class="address">4120 Larkspur Court<br>Juneau, Alaska 99801</p>
      <ul class="contact-list">
        <li>555-204-7781
          <svg class="contact-icon" viewBox="0 0 12 12" aria-hidden="true"><path d="M2.5 1h2l1 3-1.3 1a6 6 0 0 0 2.8 2.8L8 6.5l3 1v2A1.5 1.5 0 0 1 9.5 11 8.5 8.5 0 0 1 1 2.5 1.5 1.5 0 0 1 2.5 1z" fill="var(--brand-green)"/></svg>
        </li>
        <li>555-318-6642
          <svg class="contact-icon" viewBox="0 0 12 12" aria-hidden="true"><rect x="3" y="0.5" width="6" height="11" rx="1.2" fill="none" stroke="var(--brand-green)" stroke-width="1.3"/><circle cx="6" cy="9.3" r="0.7" fill="var(--brand-green)"/></svg>
        </li>
        <li>555-427-1903
          <svg class="contact-icon" viewBox="0 0 12 12" aria-hidden="true"><rect x="1" y="4" width="10" height="7" rx="1" fill="var(--brand-green)"/><rect x="3" y="1" width="6" height="4" fill="none" stroke="var(--brand-green)" stroke-width="1.2"/></svg>
        </li>
        <li>hello@everreadypath.com
          <svg class="contact-icon" viewBox="0 0 12 12" aria-hidden="true"><rect x="0.5" y="2" width="11" height="8" rx="1" fill="var(--brand-green)"/><path d="M1 3l5 3.5L11 3" fill="none" stroke="var(--brand-blue)" stroke-width="1"/></svg>
        </li>
        <li>everreadypath.com
          <svg class="contact-icon" viewBox="0 0 12 12" aria-hidden="true"><circle cx="6" cy="6" r="5" fill="none" stroke="var(--brand-green)" stroke-width="1.3"/><path d="M1 6h10M6 1c-2 3-2 7 0 10M6 1c2 3 2 7 0 10" fill="none" stroke="var(--brand-green)" stroke-width="0.9"/></svg>
        </li>
      </ul>
    </div>
  </section>

  <section class="card card-back" aria-label="Business card back">
    <p class="back-brand">Ever Ready Path</p>
  </section>

</body>
</html>
```